Tender / Request for Quotation response template

KELTRA58 is a small consulting company that works in management consulting with a particular emphasis on tourism, sport, major events and general commercial. our clients range from government , councils, private businesses and industry associations.

we are regularly asked to submit detailed quotes or tender responses and we use our own PowerPoint template to do so as we find it its generally easier to work with.

our website provides more detail : www.keltra58.com.au the colour of the blue in logo is #000033

our submissions range from 30 pages to 100 pages depending on the size and scale of the project - so we need flexibility with the templates.

Our submissions generally include cover page and table of contents and then
1. Project overview
2. About KELTRA58
3. The project team including bios
4. Initial Insights
5. importance of sustainability
6. Project methodology - example being
6.1 situation analysis
- research
- consultation and engagement
- relevant audits
- relevant economic analysis including graphs
- gap analysis
- SWOT
6.2 Issues and opportunities
6.3 draft report
6.4 final report
7. Case studies and previous relevant work
8. Project timeline
9. Project budget
10. Insurance and referees

we use many graphs and tables from excel and images generally sourced from the web. we also use icons as appropriate so we need graph templates - column, bar / pie etc and table templates.

the feel is on the formal corporate side given the size and scale of projects and clients but with bright and clear graphics and photos.

i have attached 2 copies of confidential submissions that we have made in recent weeks. one long form and one short form to give you an idea of the flexibility we need in the submission process.

if we are happy with the proposed PowerPoint tender submission template we would then look to have a similar one created to use in the development of the actual reports themselves .

hopefully this provides enough information but if not please reach out for more information

our logo and general format are in the attached examples

Target Market(s)

government, council, corporates and private businesses

Industry/Entity Type

management consulting with emphasis on tourism sport major events nd general commerical

• we usually use calbiri but open to other standard microsoft off the shelf fonts

Colors
0054AA
0677BA
7BADD7
CADEEF
E8F1F8
0094D4
00A9DD
6FCCEA
C7EBF8
E9F6FB

Requirements
Must have
• page for each of the sections detailed in the project brief. image placement - small and large, table and graph formats,

```html
<!DOCTYPE html>
<html lang="en">
<head>
<meta charset="UTF-8">
<title>KELTRA58 – Tender Response Cover</title>
<link rel="stylesheet" href="https://fonts.googleapis.com/css2?family=Montserrat:wght@400;700&family=Open+Sans:wght@400&display=swap">
<style>
  :root {
    --navy-deep: #00276a;
    --navy-mid: #01377f;
    --navy-light: #034a90;
    --white: #ffffff;
    --divider: rgba(255, 255, 255, 0.12);
  }
  * { margin: 0; padding: 0; box-sizing: border-box; }
  html, body {
    width: 1200px;
    height: 900px;
    overflow: hidden;
  }
  .cover {
    position: relative;
    width: 1200px;
    height: 900px;
    background: linear-gradient(160deg, var(--navy-deep) 0%, var(--navy-mid) 45%, var(--navy-light) 100%);
    color: var(--white);
  }
  .brand {
    position: absolute;
    left: 120px;
    top: 325px;
    width: 180px;
    display: flex;
    flex-direction: column;
    align-items: center;
  }
  .brand-circle {
    width: 176px;
    height: 176px;
    border: 4px solid var(--white);
    border-radius: 50%;
  }
  .brand-name {
    margin-top: 18px;
    font-family: "Open Sans", sans-serif;
    font-weight: 400;
    font-size: 58px;
    line-height: 1;
    letter-spacing: 1px;
    white-space: nowrap;
  }
  .divider {
    position: absolute;
    left: 428px;
    top: 322px;
    width: 2px;
    height: 296px;
    background: var(--divider);
  }
  .heading {
    position: absolute;
    left: 517px;
    top: 405px;
  }
  .project-title {
    font-family: "Montserrat", sans-serif;
    font-weight: 700;
    font-size: 48px;
    line-height: 1;
    letter-spacing: 0.3px;
  }
  .project-subtext {
    margin-top: 36px;
    font-family: "Montserrat", sans-serif;
    font-weight: 400;
    font-size: 26px;
    line-height: 1;
  }
</style>
</head>
<body>
  <main class="cover">
    <div class="brand">
      <div class="brand-circle"></div>
      <div class="brand-name">KELTRA58</div>
    </div>
    <div class="divider"></div>
    <div class="heading">
      <h1 class="project-title">PROJECT TITLE HERE</h1>
      <p class="project-subtext">SUBTEXT HERE</p>
    </div>
  </main>
</body>
</html>
```